Menu Board and Flyer for a Poke Restaurant

We need for our new Menu board for a Poke restaurant. There will be 2 separate boards. 1 Board for Speciality items, the second for "Build your Own". The menu boards will be installed on a wall.

The first board is going to be 36 W x 48 H inches. The second board will be 72 W x 48 H inches.

I would also like to consolidate the board into a one Page menu flyer that can be printed on an 11 inches x 14 inches Page.

The goal is to have customers focus on the ease of ordering.
We have attached a sample design idea for reference and our logo options. Including the logo is optional.

I have included some sample menus by other companies as attachment and referance.

Files need to include any special fonts used in the design.

Target Market(s)

Young Professionals who love eating healthy, trendy, delicious new food options.

Industry/Entity Type

Fast Food Restaurant

Font styles to use
Serif
Sans Serif

Requirements
Must have
• Simple
• Clean design - NOT busy
• Fun
• Easy to follow
• Highlight a step by step ordering process.
• Light background color
• Files need to include any special fonts used in the design.
Should not have
• script fonts

```html
<!DOCTYPE html>
<html lang="en">
<head>
<meta charset="utf-8">
<title>Coastline Pokehouse Menu</title>
<link href="https://fonts.googleapis.com/css2?family=Josefin+Sans:wght@300;400&family=Advent+Pro:wght@300;400&family=Questrial&display=swap" rel="stylesheet">
<style>
  :root{
    --backdrop:#e7e7e5;
    --paper-top:#ffffff;
    --paper-bottom:#eef0f0;
    --ink:#1b1b1b;
    --rule:#4a4a4a;
    --soft-ink:#3a3a3a;
  }
  *{margin:0;padding:0;box-sizing:border-box}
  html,body{width:1200px;height:1000px;overflow:hidden;background:var(--backdrop)}
  .stage{position:relative;width:1200px;height:1000px}
  .menu-card{position:absolute;left:338px;top:60px;width:526px;height:867px;
    background:linear-gradient(160deg,var(--paper-top) 55%,var(--paper-bottom));
    box-shadow:0 2px 8px rgba(0,0,0,.12);color:var(--ink)}
  .abs{position:absolute}

  /* brand */
  .brand{position:absolute;left:395px;top:16px;width:118px;height:100px;display:flex;align-items:center;justify-content:center}
  .brand-ring{position:absolute;left:9px;top:0;width:100px;height:100px;border:1.5px solid var(--ink);border-radius:50%}
  .brand-name{position:relative;font-family:"Josefin Sans",sans-serif;font-weight:400;font-size:14px;letter-spacing:1px;text-align:center;line-height:1.25;background:var(--paper-top);padding:2px 0}

  /* section headings */
  .section-title{font-family:"Josefin Sans",sans-serif;font-weight:400;letter-spacing:3px;white-space:nowrap}
  .title-rule{position:absolute;height:1px;background:var(--rule)}

  /* steps */
  .step-num{font-family:"Advent Pro",sans-serif;font-weight:400;line-height:1}
  .step-label{font-family:"Josefin Sans",sans-serif;line-height:1;white-space:nowrap}
  .step-label small{display:block;font-size:6px;letter-spacing:.5px;margin-bottom:2px}
  .step-label.align-right{text-align:right}

  .box{position:absolute;border-right:1px solid var(--rule);border-bottom:1px solid var(--rule)}
  .box::before{content:"";position:absolute;top:0;left:var(--gap,0);right:var(--gap-right,0);border-top:1px solid var(--rule)}
  .box::after{content:"";position:absolute;left:0;top:var(--drop,0);bottom:0;border-left:1px solid var(--rule)}
  .box.label-right{border-right:none}
  .box.label-right .side{position:absolute;right:0;top:var(--drop-right,0);bottom:0;border-right:1px solid var(--rule)}

  .item-grid{position:absolute;display:grid;font-family:"Advent Pro",sans-serif;font-weight:400;text-transform:uppercase;color:var(--soft-ink);white-space:nowrap}
  .style-head{font-family:"Questrial",sans-serif;text-transform:none;color:var(--ink);font-weight:400}

  .small-items{font-size:8.5px;line-height:1.15;letter-spacing:.2px}
  .big-items{font-size:14px;line-height:21px;letter-spacing:.4px}
</style>
</head>
<body>
<div class="stage">
  <div class="menu-card">

    <div class="brand">
      <div class="brand-ring"></div>
      <div class="brand-name">Coastline<br>Pokehouse</div>
    </div>

    <!-- BUILD YOUR OWN -->
    <div class="title-rule" style="left:40px;top:90px;width:67px"></div>
    <div class="section-title abs" style="left:118px;top:76px;font-size:25px">BUILD YOUR OWN</div>

    <!-- Step 1 style -->
    <div class="step-num abs" style="left:41px;top:124px;font-size:30px">1</div>
    <div class="step-label abs" style="left:56px;top:120px;font-size:13px"><small>CHOOSE YOUR</small>STYLE</div>
    <div class="box" style="left:57px;top:133px;width:128px;height:88px;--gap:40px;--drop:12px"></div>
    <div class="item-grid small-items" style="left:66px;top:149px;grid-template-columns:56px 60px;row-gap:8px">
      <div><span class="style-head">classic bowl</span><br>REGULAR OR<br>LARGE</div>
      <div><span class="style-head">crunchy bowl</span><br>ONE SIZE<br>TOSTADA</div>
      <div><span class="style-head">taco style</span><br>POKE SERVED<br>TACO STYLE</div>
      <div><span class="style-head">just poke</span><br>NO BASE. 1LB OF<br>YOUR FAVORITE</div>
    </div>

    <!-- Step 2 fish -->
    <div class="step-num abs" style="left:44px;top:232px;font-size:26px">2</div>
    <div class="step-label abs" style="left:56px;top:229px;font-size:13px"><small>CHOOSE YOUR</small>FISH</div>
    <div class="box" style="left:57px;top:243px;width:128px;height:63px;--gap:32px;--drop:12px"></div>
    <div class="item-grid small-items" style="left:69px;top:257px;grid-template-columns:54px 60px">
      <div>AHI</div><div>TUNA</div>
      <div>SALMON</div><div>HAMACHI</div>
      <div>SPICY TUNA</div><div>SHRIMP</div>
      <div>SCALLOP</div><div></div>
    </div>

    <!-- Step 3 toppings -->
    <div class="step-num abs" style="left:218px;top:124px;font-size:26px">3</div>
    <div class="step-label abs" style="left:233px;top:120px;font-size:13px"><small>CHOOSE YOUR</small>TOPPINGS</div>
    <div class="box" style="left:233px;top:131px;width:223px;height:84px;--gap:80px;--drop:14px"></div>
    <div class="item-grid small-items" style="left:249px;top:153px;grid-template-columns:71px 80px 60px">
      <div>CRISPY ONION</div><div>GREEN ONION</div><div>SWEET</div>
      <div>ONION</div><div>MASAGO</div><div>CILANTRO</div>
      <div>CUCUMBER</div><div>CORN</div><div>COCONUT</div>
      <div>FLAKES</div><div>HAWAIIAN</div><div>SEA SALT</div>
      <div>CHILLI</div><div>FLAKES</div><div>OGO</div>
    </div>

    <!-- Step 4 sauce -->
    <div class="step-num abs" style="left:219px;top:228px;font-size:26px">4</div>
    <div class="step-label abs" style="left:233px;top:228px;font-size:13px"><small>CHOOSE YOUR</small>SAUCE</div>
    <div class="box" style="left:233px;top:242px;width:223px;height:62px;--gap:55px;--drop:14px"></div>
    <div class="item-grid small-items" style="left:244px;top:261px;grid-template-columns:71px 80px 68px">
      <div>SESAME SHOYU</div><div>SIRACHA AIOLI</div><div>PONZU</div>
      <div>SWEET SHOYU</div><div>WASABI SHOYU</div><div>SWEET CHILI</div>
      <div>CHILI UME</div><div>GINGER SCALLION</div><div>WASABI CREME</div>
    </div>

    <!-- Step 5 base -->
    <div class="step-num abs" style="left:44px;top:320px;font-size:28px">5</div>
    <div class="step-label abs" style="left:58px;top:326px;font-size:13px"><small>CHOOSE YOUR</small>BASE</div>
    <div class="box" style="left:112px;top:322px;width:344px;height:27px;--drop:0"></div>
    <div class="item-grid small-items" style="left:127px;top:330px;grid-template-columns:72px 79px 74px 80px;font-size:9.5px">
      <div>WHITE RICE</div><div>BROWN RICE</div><div>BLACK RICE</div><div>MIXED GREENS</div>
    </div>

    <!-- HOUSE SPECIALTIES -->
    <div class="title-rule" style="left:30px;top:378px;width:84px"></div>
    <div class="title-rule" style="left:407px;top:378px;width:86px"></div>
    <div class="section-title abs" style="left:124px;top:364px;font-size:24px;letter-spacing:.8px">HOUSE SPECIALTIES</div>

    <!-- Specialty 1 -->
    <div class="step-num abs" style="left:100px;top:410px;font-size:72px">1</div>
    <div class="step-label abs" style="left:125px;top:417px;font-size:24px"><small style="font-size:7px">CHOOSE A</small>SPECIALTY</div>
    <div class="box" style="left:129px;top:422px;width:270px;height:107px;--gap:120px;--drop:26px"></div>
    <div class="item-grid big-items" style="left:141px;top:460px;grid-template-columns:124px 126px">
      <div>LAVA HOT</div><div>CRAZY KIMCHI</div>
      <div>CLASSIC HAWAIIAN</div><div>WASABI LOVER</div>
      <div>SWEET AND SPICY</div><div>GINGER GINGER</div>
    </div>

    <!-- Style 2 -->
    <div class="step-label align-right abs" style="right:124px;top:544px;font-size:24px"><small style="font-size:7px">CHOOSE YOUR</small>STYLE</div>
    <div class="step-num abs" style="left:404px;top:557px;font-size:56px">2</div>
    <div class="box label-right" style="left:131px;top:558px;width:268px;height:163px;--gap-right:68px;--drop:0">
      <span class="side" style="--drop-right:24px"></span>
    </div>
    <div class="item-grid" style="left:147px;top:583px;grid-template-columns:112px 140px;row-gap:5px;font-size:14px;line-height:20px;letter-spacing:.4px">
      <div><span class="style-head" style="font-size:15.5px">classic bowl</span><br>REGULAR OR<br>LARGE</div>
      <div><span class="style-head" style="font-size:15.5px">crunchy bowl</span><br>ONE SIZE,<br>TOSTADA STYLE</div>
      <div><span class="style-head" style="font-size:15.5px">surfer style</span><br>POKE SERVED<br>TACO STYLE</div>
      <div><span class="style-head" style="font-size:15.5px">just poke</span><br>NO BASE, 1LB OF<br>YOUR FAVORITE POKE</div>
    </div>

    <!-- Base 3 -->
    <div class="step-num abs" style="left:101px;top:752px;font-size:62px">3</div>
    <div class="step-label abs" style="left:129px;top:751px;font-size:22px"><small style="font-size:7px">CHOOSE YOUR</small>BASE</div>
    <div class="box" style="left:131px;top:762px;width:268px;height:70px;--gap:58px;--drop:22px"></div>
    <div class="item-grid big-items" style="left:195px;top:783px;grid-template-columns:109px 92px;line-height:20px">
      <div>WHITE RICE</div><div>BROWN RICE</div>
      <div>BLACK RICE</div><div>MIXED GREENS</div>
    </div>

  </div>
</div>
</body>
</html>
```